Marwood Holiday Jubilee 2025

We’re looking for a designer to help refresh the visual identity of our annual Christmas show while maintaining continuity from previous years. The updated design should feel festive, and warm, with a sense of celebration and anticipation. We’d like a central graphic that can be adapted for posters, social media, and digital signage, along with supporting assets for flyers and banners.

We’re open to seasonal color palettes such as rich reds, deep greens or blues, golds, silvers, or cool winter tones, and prefer typography that’s clear and elegant. The overall look should feel familiar to returning audiences while inviting and engaging for newcomers.

Two key groups: the current attenders of our congregation and the broader community in our suburb of Rochester, NY. Our congregation is made up of families, older adults, and young professionals who value faith, community and spiritual growth. The surrounding community is a fast growing friendly and family-oriented area of young professionals and longtime families.

We’re looking for a designer to help refresh the visual identity of our annual Christmas show while maintaining continuity with the theme and tone of previous years. The updated design should feel festive, and warm, with a sense of celebration and anticipation. We’d like a central graphic that can be adapted for posters, social media, and digital signage, along with supporting assets for flyers and banners.

Target Market(s)

Two key groups: the current attenders of our congregation and the broader community in our suburb of Rochester, NY. Our congregation is made up of families, older adults, and young professionals who value faith, community and spiritual growth. The surrounding community is a fast growing friendly and family-oriented area of young professionals and long time families.

Industry/Entity Type

Non-profit. Church

Font styles to use
Serif
Decorative
Script
Other font styles liked:
• Quentin

Requirements
Must have
• Sparkle, eye catching
Should not have
• must not look identical to the uploaded versions

```html
<!DOCTYPE html>
<html lang="en">
<head>
<meta charset="utf-8">
<title>Marwood Holiday Jubilee</title>
<link rel="stylesheet" href="https://fonts.googleapis.com/css2?family=Pinyon+Script&family=Roboto:wght@700&display=swap">
<style>
  :root {
    --pine-dark: #1b1f17;
    --pine-mid: #2a3326;
    --glow-strong: rgba(255, 220, 160, 0.55);
    --glow-soft: rgba(255, 214, 150, 0.22);
    --gold: #ffe2a8;
    --red-deep: #c01d10;
    --red-warm: #e2632a;
    --shadow: rgba(0, 0, 0, 0.6);
  }
  html, body {
    margin: 0;
    padding: 0;
    width: 1200px;
    height: 751px;
    overflow: hidden;
    background: var(--pine-dark);
  }
  .poster {
    position: relative;
    width: 1200px;
    height: 751px;
    overflow: hidden;
  }
  .tree-backdrop {
    position: absolute;
    inset: 0;
    background:
      radial-gradient(circle at 1080px 590px, var(--glow-strong) 0, transparent 60px),
      radial-gradient(circle at 830px 215px, var(--glow-soft) 0, transparent 34px),
      radial-gradient(circle at 925px 255px, var(--glow-soft) 0, transparent 30px),
      radial-gradient(circle at 350px 35px, var(--glow-soft) 0, transparent 28px),
      radial-gradient(circle at 140px 140px, var(--glow-soft) 0, transparent 45px),
      radial-gradient(circle at 30px 290px, var(--glow-soft) 0, transparent 45px),
      radial-gradient(circle at 1180px 310px, var(--glow-soft) 0, transparent 32px),
      radial-gradient(circle at 1040px 405px, var(--glow-soft) 0, transparent 30px),
      radial-gradient(circle at 50px 670px, var(--glow-strong) 0, transparent 42px),
      radial-gradient(circle at 40px 725px, var(--glow-strong) 0, transparent 38px),
      radial-gradient(circle at 1175px 740px, var(--glow-soft) 0, transparent 40px),
      radial-gradient(ellipse at 50% 50%, var(--pine-mid) 0%, var(--pine-dark) 75%),
      var(--pine-dark);
  }
  .artwork {
    position: absolute;
    inset: 0;
    width: 1200px;
    height: 751px;
  }
  .frame-line {
    fill: none;
    stroke: url(#warmRed);
    stroke-width: 4;
  }
  .frame-inner {
    fill: none;
    stroke: url(#warmRed);
    stroke-width: 1;
    opacity: 0.6;
  }
  .sparkle {
    fill: var(--gold);
    filter: drop-shadow(0 0 4px var(--gold));
  }
  .type-sans {
    font-family: "Roboto", "Helvetica Neue", Arial, sans-serif;
    font-weight: 700;
    fill: url(#warmRed);
  }
  .type-script {
    font-family: "Pinyon Script", "Brush Script MT", cursive;
    fill: url(#warmRed);
  }
  .lifted {
    filter: drop-shadow(2px 3px 2px var(--shadow));
  }
</style>
</head>
<body>
<main class="poster">
  <div class="tree-backdrop" role="img" aria-label="Softly blurred evergreen branches with glowing golden holiday lights"></div>

  <svg class="artwork" viewBox="0 0 1200 751" xmlns="http://www.w3.org/2000/svg">
    <defs>
      <linearGradient id="warmRed" x1="0" y1="0" x2="1" y2="1">
        <stop offset="0" stop-color="#c01d10"/>
        <stop offset="0.5" stop-color="#e2632a"/>
        <stop offset="1" stop-color="#c01d10"/>
      </linearGradient>
      <path id="star" d="M0 -10 L2 -2 L10 0 L2 2 L0 10 L-2 2 L-10 0 L-2 -2 Z"/>
    </defs>

    <path class="frame-line lifted" d="M520 159 H172 V593 H1028 V159 H678"/>
    <path class="frame-inner" d="M510 168 H181 V584 H1019 V168 H688"/>

    <use class="sparkle" href="#star" transform="translate(172 159) scale(1.2)"/>
    <use class="sparkle" href="#star" transform="translate(1028 159) scale(1.2)"/>
    <use class="sparkle" href="#star" transform="translate(172 593) scale(1.2)"/>
    <use class="sparkle" href="#star" transform="translate(1028 593) scale(1.2)"/>
    <use class="sparkle" href="#star" transform="translate(505 159) scale(0.6)"/>
    <use class="sparkle" href="#star" transform="translate(693 159) scale(0.6)"/>
    <use class="sparkle" href="#star" transform="translate(905 450) scale(0.8)"/>
    <use class="sparkle" href="#star" transform="translate(300 470) scale(0.7)"/>

    <text class="type-sans lifted church-name" x="384" y="135" font-size="31" textLength="436" lengthAdjust="spacing">ELMBROOK FELLOWSHIP CHURCH</text>
    <text class="type-script lifted presents" x="601" y="170" font-size="46" text-anchor="middle">presents</text>

    <text class="type-sans lifted title-top" x="335" y="292" font-size="92" textLength="530" lengthAdjust="spacing">MARWOOD</text>
    <text class="type-sans lifted title-middle" x="217" y="384" font-size="102" textLength="751" lengthAdjust="spacing">HOLIDAY</text>
    <text class="type-script lifted title-script" x="600" y="520" font-size="200" text-anchor="middle">Jubilee</text>

    <text class="type-sans lifted event-date" x="346" y="638" font-size="37" textLength="504" lengthAdjust="spacing">DECEMBER 13 &amp; 14  6:00PM</text>
  </svg>
</main>
</body>
</html>
```